Personal Web page for recruiter and owner of consulting firm

I work full time as a recruiter so I want a page that allows for me to support my efforts. I would like a long single page, I need to be able to upload four two minute videos, and 4 images. I also want the color scheme to match with my consulting company. I own the domain marlowfenwick.net already through wordpress . I took a shot at it myself and its terrible.

Target Market(s)

Potential clients

Industry/Entity Type

Management Consulting

Logo Text

marlow fenwick

Font styles to use
Serif

Requirements
Must have
• Must in color scheme go well with my consulting company logo attached
• Must be able to upload 4 two minute videos and 4 images (photos of me)
• Single long scroll page
• Modern and clean
Nice to have
• Easy for me to update videos images and text without complex coding
Should not have
• I want the design and feel to go well with my logos not exactly replicate it

```html
<!DOCTYPE html>
<html lang="en">
<head>
<meta charset="utf-8">
<title>Fenwick Strategies</title>
<link href="https://fonts.googleapis.com/css2?family=Roboto:wght@300;400;500;700&display=swap" rel="stylesheet">
<style>
:root{
  --navy:#2f4b8c;
  --navy-dark:#2b4586;
  --sky:#5ba7de;
  --sky-soft:#7db8e6;
  --ink:#333a44;
  --muted:#7b828c;
  --line:#dde1e7;
  --panel:#f4f6f9;
  --white:#ffffff;
}
*{box-sizing:border-box;margin:0;padding:0}
html,body{width:1200px;height:3364px;overflow:hidden}
body{font-family:"Roboto",Arial,sans-serif;color:var(--ink);background:var(--white);position:relative}
.section{position:absolute;left:0;width:1200px}
.abs{position:absolute}
.center{left:0;width:1200px;text-align:center}
.sec-title{font-size:24px;font-weight:700;color:var(--navy);letter-spacing:.5px;text-transform:uppercase}
.sec-title span{color:var(--sky);font-weight:500}
.sec-sub{font-size:12px;color:var(--muted)}
.body-text{font-size:12px;line-height:22px;color:var(--muted)}
.btn-ghost{position:absolute;border:1px solid rgba(255,255,255,.7);color:var(--white);font-size:12px;text-transform:uppercase;display:flex;align-items:center;justify-content:center;letter-spacing:.3px}

/* header */
.site-header{top:0;height:97px;background:var(--white);box-shadow:0 1px 4px rgba(0,0,0,.08);z-index:2}
.brand{left:85px;top:34px;font-size:24px;line-height:30px;font-weight:400;color:var(--ink);white-space:nowrap}
.nav a{position:absolute;top:43px;font-size:11px;font-weight:500;color:var(--ink);text-decoration:none;text-transform:uppercase}
.nav a.active{color:var(--sky)}

/* hero */
.hero{top:97px;height:509px;background:linear-gradient(100deg,#8a6a4a 0%,#5b4a3e 30%,#3a3a40 60%,#1e2228 100%)}
.hero-title{top:165px;font-size:40px;font-weight:400;color:var(--white);letter-spacing:1px}
.hero-text{top:234px;left:270px;width:660px;text-align:center;font-size:12px;line-height:25px;color:#eee}
.dots{top:478px;left:560px;display:flex;gap:8px}
.dots i{width:12px;height:12px;border:2px solid var(--white);border-radius:50%;display:block}
.dots i.on{background:var(--white)}

/* about */
.about{top:606px;height:489px;background:linear-gradient(90deg,#f2f3f5,#e6e8ec)}
.about-photo{left:85px;top:22px;width:465px;height:467px;background:linear-gradient(160deg,#e9eaec,#b9bcc2 60%,#8e8f94)}
.about-title{left:603px;top:60px;font-size:30px;font-weight:700;color:var(--navy)}
.about-title span{color:var(--sky);font-weight:500}
.about-text{left:603px;width:490px}
.btn-light{position:absolute;border:1px solid #c8ccd2;background:#eef0f3;color:var(--muted);font-size:12px;text-transform:uppercase;display:flex;align-items:center;justify-content:center}

/* services */
.services{top:1095px;height:453px;background:var(--white)}
.service{top:153px;width:320px;text-align:center}
.service-icon{width:130px;height:130px;margin:0 auto;border-radius:50%;border:2px solid var(--navy);padding:5px}
.service-icon div{width:100%;height:100%;border-radius:50%;background:var(--navy);display:flex;align-items:center;justify-content:center}
.service.alt .service-icon{border-color:var(--sky)}
.service.alt .service-icon div{background:var(--sky)}
.service-name{margin-top:24px;font-size:15px;font-weight:700;color:var(--navy)}
.service.alt .service-name{color:var(--sky);font-weight:500}
.service-text{margin-top:10px}

/* careers */
.careers{top:1548px;height:399px;background:linear-gradient(90deg,#a6cbec,#6fb0e2 40%,#6aaee1 70%,#9cc6ea)}
.careers-title{top:100px;font-size:33px;color:var(--white);font-weight:400}
.careers-text{top:165px;left:225px;width:750px;text-align:center;font-size:12px;line-height:25px;color:#f3f8fd}

/* video */
.videos{top:1947px;height:359px;background:var(--white)}
.thumb{top:126px;width:247px;height:183px;display:flex;align-items:center;justify-content:center}
.play{width:54px;height:54px;border-radius:50%;border:2px solid rgba(255,255,255,.8)}

/* blog */
.blog{top:2306px;height:549px;background:var(--panel)}
.card{top:123px;width:499px;height:391px;background:var(--white);box-shadow:0 1px 3px rgba(0,0,0,.06)}
.card-img{height:242px}
.card-title{margin:26px 0 0 20px;font-size:13px;font-weight:700;color:var(--ink);text-transform:uppercase}
.card-meta{margin:10px 0 0 20px;font-size:12px;color:var(--sky);display:flex;gap:14px;align-items:center}
.card-meta u{text-decoration:underline}
.card-text{margin:12px 20px 0}

/* contact */
.contact{top:2855px;height:447px;background:var(--white)}
.field{position:absolute;background:#f1f3f6;border:1px solid #e3e6eb;font-size:11px;color:var(--muted);padding:10px 12px}
.submit{position:absolute;left:90px;top:377px;width:105px;height:38px;background:var(--sky);color:var(--white);font-size:12px;font-weight:700;display:flex;align-items:center;justify-content:center}
.label{font-size:13px;color:var(--sky);text-transform:uppercase;letter-spacing:.5px}
.info{font-size:11px;line-height:22px;color:var(--muted)}
.social{position:absolute;top:362px;width:36px;height:36px;border-radius:50%;border:1px solid #9aa0a8}

/* footer */
.site-footer{top:3302px;height:62px;background:var(--navy-dark);color:#dfe6f3;font-size:12px;display:flex;align-items:center;justify-content:center}
</style>
</head>
<body>

<header class="section site-header">
  <div class="abs brand">Fenwick Strategies</div>
  <nav class="nav">
    <a class="active" style="left:438px">Home</a>
    <a style="left:530px">About Us</a>
    <a style="left:643px">Services</a>
    <a style="left:754px">Careers</a>
    <a style="left:862px">Video</a>
    <a style="left:953px">Blog</a>
    <a style="left:1040px">Contact Us</a>
  </nav>
</header>

<section class="section hero" role="img" aria-label="Person working on a laptop at a wooden table with coffee cups">
  <h1 class="abs center hero-title">FENWICK STRATEGIES</h1>
  <p class="abs hero-text">Sed ut perspiciatis unde omnis iste natus error sit voluptatem accusantium doloremque laudantium, totam rem ipsa quae ab illo inventore veritatis et quasi architecto beatae vitae dicta sunt explicabo.</p>
  <div class="btn-ghost" style="left:500px;top:309px;width:200px;height:45px;font-weight:500">Read More Info</div>
  <div class="abs dots"><i class="on"></i><i></i><i></i><i></i></div>
</section>

<section class="section about">
  <div class="abs about-photo" role="img" aria-label="Smiling consultant seated in a white chair with a laptop"></div>
  <h2 class="abs about-title">ABOUT <span>US</span></h2>
  <p class="abs body-text about-text" style="top:120px">Sed ut perspiciatis unde omnis iste natus error sit voluptatem accusantium doloremque laudantium, totam rem aperiam, eaque ipsa quae ab illo inventore veritatis et quasi arch itecto beatae vitae dicta sunt explicabo. Nemo enim ipsam voluptatem quia vol uptas sit aspernatur aut odit aut fugit, sed quia consequuntur magni dolores eos qui ratione voluptatem sequi nesciunt.</p>
  <p class="abs body-text about-text" style="top:265px">Nemo enim ipsam voluptatem quia voluptas sit aspernatur aut odit aut fugit, sed quia consequuntur magni dolores eos qui ratione voluptatem sequi nesciunt inventore veri atis et quasi architecto beatae vitae dicta sunt explicabo.</p>
  <div class="btn-light" style="left:603px;top:370px;width:232px;height:47px">Click Here For More Info</div>
</section>

<section class="section services">
  <h2 class="abs center sec-title" style="top:41px">OUR <span>SERVICES</span></h2>
  <p class="abs center sec-sub" style="top:82px">Sed ut perspiciatis unde omnis iste natus error sit voluptatem accusantium dolorem queilaudantium</p>

  <div class="abs service" style="left:93px">
    <div class="service-icon"><div>
      <svg width="54" height="46" viewBox="0 0 54 46"><rect x="18" y="2" width="18" height="10" rx="2" fill="none" stroke="#fff" stroke-width="4"/><rect x="2" y="10" width="50" height="34" rx="4" fill="#fff"/><rect x="23" y="22" width="8" height="7" fill="#2f4b8c"/></svg>
    </div></div>
    <div class="service-name">JOB</div>
    <p class="body-text service-text">Sed ut perspiciatis unde omnis iste natus error sit<br>voluptatem accusantium doloremque laudantium,<br>beatae vitae dicta sunt explicabo</p>
  </div>

  <div class="abs service alt" style="left:439px">
    <div class="service-icon"><div>
      <svg width="60" height="56" viewBox="0 0 60 56"><circle cx="17" cy="14" r="7" fill="#fff"/><circle cx="43" cy="14" r="7" fill="#fff"/><circle cx="30" cy="22" r="9" fill="#fff"/><path d="M4 38c0-8 6-13 13-13M56 38c0-8-6-13-13-13" stroke="#fff" stroke-width="4" fill="none"/><circle cx="30" cy="40" r="9" fill="none" stroke="#fff" stroke-width="4"/><path d="M37 46l9 8" stroke="#fff" stroke-width="5"/></svg>
    </div></div>
    <div class="service-name">RECRUITER</div>
    <p class="body-text service-text">Sed ut perspiciatis unde omnis iste natus error sit<br>voluptatem accusantium doloremque laudantium,<br>beatae vitae dicta sunt explicabo</p>
  </div>

  <div class="abs service" style="left:784px">
    <div class="service-icon"><div>
      <svg width="60" height="54" viewBox="0 0 60 54"><circle cx="14" cy="12" r="7" fill="#fff"/><circle cx="46" cy="12" r="7" fill="#fff"/><path d="M4 40V28c0-5 4-8 10-8s10 3 10 8v12M36 40V28c0-5 4-8 10-8s10 3 10 8v12" fill="#fff"/><rect x="20" y="30" width="20" height="4" fill="#fff"/><rect x="8" y="42" width="44" height="4" fill="#fff"/></svg>
    </div></div>
    <div class="service-name">CONSULTING</div>
    <p class="body-text service-text">Sed ut perspiciatis unde omnis iste natus error sit<br>voluptatem accusantium doloremque laudantium,<br>beatae vitae dicta sunt explicabo</p>
  </div>
</section>

<section class="section careers" role="img" aria-label="Blue-tinted photo of colleagues shaking hands in an office">
  <h2 class="abs center careers-title">OUR CAREERS</h2>
  <p class="abs careers-text">Sed ut perspiciatis unde omnis iste natus error sit voluptatem accusantium doloremque laudantium, totam rem aperiam, eaque ipsa quae ab illo inventore veritatis et quasi architecto beatae vitae dicta sunt explicabo. Nemo enim ipsam voluptatem quia voluptas sit sed quia consequuntur magni dolores eos qui ratione voluptatem sequi nesciunt</p>
  <div class="btn-ghost" style="left:485px;top:267px;width:231px;height:47px">Click Here For More Info</div>
</section>

<section class="section videos">
  <h2 class="abs center sec-title" style="top:40px">LATEST <span>VIDEO</span></h2>
  <p class="abs center sec-sub" style="top:80px">Sed ut perspiciatis unde omnis iste natus error sit voluptatem accusantium dolorem queilaudantium</p>
  <div class="abs thumb" style="left:85px;background:linear-gradient(135deg,#c9d6e6,#6c87ad)" role="img" aria-label="Video: team meeting around a table"><div class="play"></div></div>
  <div class="abs thumb" style="left:345px;background:linear-gradient(135deg,#8a8f98,#3d4249)" role="img" aria-label="Video: hand touching a network of candidate icons"><div class="play"></div></div>
  <div class="abs thumb" style="left:606px;background:linear-gradient(135deg,#6f5a4a,#2f2a2a)" role="img" aria-label="Video: hands using a phone and laptop"><div class="play"></div></div>
  <div class="abs thumb" style="left:866px;background:linear-gradient(135deg,#41506a,#9aa6b8)" role="img" aria-label="Video: businessman holding figures of people"><div class="play"></div></div>
</section>

<section class="section blog">
  <h2 class="abs center sec-title" style="top:40px">RECENT <span>BLOG</span></h2>
  <p class="abs center sec-sub" style="top:80px">Sed ut perspiciatis unde omnis iste natus error sit voluptatem accusantium dolorem queilaudantium</p>
  <article class="abs card" style="left:85px">
    <div class="card-img" style="background:linear-gradient(180deg,#f2f3f5,#c9ccd2 60%,#3a3d44)" role="img" aria-label="Row of candidates silhouetted with a magnifying glass"></div>
    <h3 class="card-title">Sed ut perspiciatis unde omnis</h3>
    <div class="card-meta"><u>02 Feb 2017</u><span style="color:var(--muted)">|</span><u>Comments</u></div>
    <p class="body-text card-text">Sed ut perspiciatis unde omnis iste natus error sit voluptatem accusantium dolo veritatis et quasi architecto beatae vitae dicta sunt explicabo.</p>
  </article>
  <article class="abs card" style="left:614px">
    <div class="card-img" style="background:linear-gradient(135deg,#d8dbe0,#7d828b 55%,#2c2f35)" role="img" aria-label="Businessman touching a recruitment network graphic"></div>
    <h3 class="card-title">Sed ut perspiciatis unde omnis</h3>
    <div class="card-meta"><u>02 Feb 2017</u><span style="color:var(--muted)">|</span><u>Comments</u></div>
    <p class="body-text card-text">Sed ut perspiciatis unde omnis iste natus error sit voluptatem accusantium dolo veritatis et quasi architecto beatae vitae dicta sunt explicabo.</p>
  </article>
</section>

<section class="section contact">
  <h2 class="abs center sec-title" style="top:35px">CONTACT <span>US</span></h2>
  <p class="abs center sec-sub" style="top:76px">Sed ut perspiciatis unde omnis iste natus error sit voluptatem accusantium dolorem queilaudantium</p>
  <div class="field" style="left:85px;top:146px;width:247px;height:38px">Name :</div>
  <div class="field" style="left:343px;top:146px;width:245px;height:38px">Email :</div>
  <div class="field" style="left:85px;top:195px;width:247px;height:38px">Phone :</div>
  <div class="field" style="left:343px;top:195px;width:245px;height:38px">Subjects :</div>
  <div class="field" style="left:85px;top:245px;width:503px;height:108px">Message :</div>
  <div class="submit">SUBMIT</div>

  <p class="abs info" style="left:621px;top:138px;width:480px">Sed ut perspiciatis unde omnis iste natus error sit voluptatem accusantium doloremque laudantium, totam rem aperiam, eaque ipsa quae ab illo inventore veritatis et quasi archi-tecto beatae vitae dicta sunt explicabo latem sequi nesciunt.</p>
  <div class="abs label" style="left:621px;top:233px">Address</div>
  <p class="abs info" style="left:621px;top:256px">244 5th Lorem Ipsum dummy Text<br>Lorem Ipsum</p>
  <div class="abs label" style="left:621px;top:341px">Phone</div>
  <p class="abs info" style="left:621px;top:368px">Mobile : (000)-121-1231</p>
  <div class="abs label" style="left:875px;top:233px">Email Address</div>
  <p class="abs info" style="left:875px;top:256px">General : info@marlowfenwick.net<br>Office : info@marlowfenwick.net</p>
  <div class="abs label" style="left:875px;top:323px">Follow Us</div>
  <span class="social" style="left:870px"></span>
  <span class="social" style="left:912px"></span>
  <span class="social" style="left:954px"></span>
  <span class="social" style="left:996px"></span>
  <span class="social" style="left:1038px"></span>
</section>

<footer class="section site-footer">© Copyright 2017 Marlow Fenwick.All Rights Reserved</footer>

</body>
</html>
```